Bathroom Renovation Business card design needed

Bathroom, Kitchen & Laundry Renovations
Mainly complete bathroom renovations

Target Market(s)

people wanting a total bathroom renovations and other trades people

Industry/Entity Type

Business

Contact Information for Business Card

Dalby Bathrooms
Tomas Dalby
Mobile: 0438 207615
Licence no: 764519K
Email: dalbybathrooms@mailnest.example

Logo styles of interest
Lettermark Logo
Requirements
Must have
• the business card should be predominantly blue
Nice to have
• the DB logo featured in the business card will be used on tshirts,tax invoices , letters etc so the DB will be the main feature, and preferably blue
Should not have
• We found the red DB logo through google images. We understand that it cannot be exactly the same but we like how the DB is linked. The example business card is something we designed but we prefer more blues. Maybe different shades of blue.

```html
<!DOCTYPE html>
<html lang="en">
<head>
<meta charset="utf-8">
<title>Dalby Bathrooms – Business Card</title>
<link href="https://fonts.googleapis.com/css2?family=Open+Sans:wght@300;400;700&display=swap" rel="stylesheet">
<style>
  :root {
    --stage: #0d4a72;
    --card-white: #fbfbfb;
    --brand-blue: #4a9fda;
    --brand-blue-deep: #3a8fcb;
    --band-blue: #c6dcf0;
    --text-grey: #555a60;
    --icon-grey: #777b80;
    --logo-silver: #e9ecef;
  }
  * { margin: 0; padding: 0; box-sizing: border-box; }
  html, body { width: 1200px; height: 750px; overflow: hidden; }
  body {
    background: var(--stage);
    font-family: "Open Sans", Arial, sans-serif;
    position: relative;
  }
  .card {
    position: absolute;
    top: 215px;
    width: 540px;
    height: 320px;
    overflow: hidden;
    box-shadow: 0 14px 30px rgba(0, 0, 0, 0.45);
  }

  /* Front */
  .card-front { left: 45px; background: var(--card-white); }
  .card-front .bottom-band {
    position: absolute; left: 0; right: 0; bottom: 0; height: 42px;
    background: linear-gradient(to bottom, #dde9f5, var(--band-blue));
  }
  .brand-line {
    position: absolute; left: 0; bottom: 74px;
    display: flex; align-items: center; gap: 10px;
  }
  .brand-square {
    width: 40px; height: 22px; background: var(--brand-blue);
  }
  .brand-name {
    font-weight: 300; font-size: 26px; color: var(--brand-blue);
    letter-spacing: -0.3px; white-space: nowrap;
  }
  .contact-panel {
    position: absolute; top: 0; right: 0; width: 250px; height: 278px;
    background: #fff;
    box-shadow: -4px 4px 12px rgba(0, 0, 0, 0.18);
    border-bottom-left-radius: 10px;
    padding: 26px 14px 0 18px;
  }
  .person-name {
    font-weight: 300; font-size: 30px; color: var(--brand-blue);
    margin-bottom: 14px; letter-spacing: -0.5px; white-space: nowrap;
  }
  .contact-item { margin-bottom: 14px; padding-left: 30px; position: relative; }
  .contact-label {
    font-weight: 700; font-size: 15px; color: var(--brand-blue-deep);
  }
  .contact-value {
    font-size: 12px; color: var(--text-grey); white-space: nowrap;
  }
  .contact-value.is-email { font-size: 10.5px; }
  .contact-icon {
    position: absolute; left: 0; top: 20px; width: 22px; height: 18px;
  }
  .contact-prefix {
    position: absolute; left: 0; top: 19px;
    font-size: 14px; font-style: italic; color: var(--text-grey);
  }

  /* Back */
  .card-back {
    left: 615px;
    background: linear-gradient(160deg, #5aaee2, var(--brand-blue) 60%, #3f93cf);
  }
  .world-map {
    position: absolute; left: 70px; top: 40px; width: 420px; height: 190px;
    background: radial-gradient(ellipse at center, rgba(160, 205, 238, 0.55), rgba(122, 184, 228, 0) 70%);
  }
  .card-back .bottom-band {
    position: absolute; left: 0; right: 0; bottom: 0; height: 70px;
    background: linear-gradient(to bottom, #5aa8de, #8cc4ea 50%, #64aee0);
    border-top: 1px solid rgba(255, 255, 255, 0.35);
  }
  .monogram {
    position: absolute; left: 0; right: 0; top: 70px;
    text-align: center;
    font-weight: 700; font-size: 140px; line-height: 1;
    color: var(--logo-silver); letter-spacing: -6px;
  }
</style>
</head>
<body>
  <section class="card card-front">
    <div class="brand-line">
      <span class="brand-square"></span>
      <span class="brand-name">Dalby Bathrooms</span>
    </div>
    <div class="bottom-band"></div>
    <div class="contact-panel">
      <h1 class="person-name">Tomas Dalby</h1>
      <div class="contact-item">
        <svg class="contact-icon" viewBox="0 0 24 18" aria-hidden="true">
          <rect x="2" y="3" width="18" height="12" fill="none" stroke="var(--icon-grey)" stroke-width="1.2"/>
          <polyline points="2,3 11,10 20,3" fill="none" stroke="var(--icon-grey)" stroke-width="1.2"/>
        </svg>
        <div class="contact-label">Email</div>
        <div class="contact-value is-email">dalbybathrooms@mailnest.example</div>
      </div>
      <div class="contact-item">
        <svg class="contact-icon" viewBox="0 0 24 18" aria-hidden="true">
          <rect x="7" y="1" width="9" height="16" rx="1.5" fill="none" stroke="var(--icon-grey)" stroke-width="1.2"/>
          <line x1="10" y1="14.5" x2="13" y2="14.5" stroke="var(--icon-grey)" stroke-width="1.2"/>
        </svg>
        <div class="contact-label">Mobile</div>
        <div class="contact-value">0438 207615</div>
      </div>
      <div class="contact-item">
        <span class="contact-prefix">no:</span>
        <div class="contact-label">Licence</div>
        <div class="contact-value">764519K</div>
      </div>
    </div>
  </section>

  <section class="card card-back">
    <div class="world-map" role="img" aria-label="Faint dotted world map"></div>
    <div class="bottom-band"></div>
    <div class="monogram">DB</div>
  </section>
</body>
</html>
```